design for locksmith business

I need new logo, letterhead, business card and envelope designed for new mobile locksmith business.
Start off with a Logo but keep in mind that i want it to be used on all obove things listed.
Once a good logo is designed i will be more than happy to increase payment to have all listed designed.
Business Name: Harbourgate Locksmiths
Slogan (We come to you 24/7)
www.harbourgatelocksmiths.com.au
dom@harbourgatelocksmiths.com.au
Phone: TBA
Mobile Locksmith business
Services Offered:
Residential
Commercial
Automotive
Safes
24/7 Fast Reliable Service

I think the logo should be modern and maybe show that we are a mobile service so maybe add underneath in small letters (We come to you 24/7)

Also keep in mind the design will be uniform across all business card, letterheads, Envelopes and web pages.

Once i have found a good logo i am more than happy to increase payment to have the other things (Business cards etc... designed to go with the logo.

Target Market(s)

Residential and commercial clients needing lock repairs on site

Industry/Entity Type

Locksmith

```html
<!DOCTYPE html>
<html lang="en">
<head>
<meta charset="utf-8">
<title>Harbourgate Locksmiths Stationery</title>
<link href="https://fonts.googleapis.com/css2?family=Roboto:wght@400;700;900&display=swap" rel="stylesheet">
<style>
  :root {
    --red: #c01f2f;
    --ink: #3b3b3b;
    --edge: #2e2e2e;
    --paper: #ffffff;
    --ground: #dcdcdc;
    --shadow: rgba(0,0,0,0.28);
  }
  * { box-sizing: border-box; margin: 0; padding: 0; }
  html, body { width: 1200px; height: 900px; overflow: hidden; }
  body {
    background: var(--ground);
    font-family: "Roboto", Arial, sans-serif;
    position: relative;
    color: var(--ink);
  }
  .sheet {
    position: absolute;
    background: var(--paper);
    box-shadow: 3px 4px 6px var(--shadow);
    overflow: hidden;
  }
  .brand { display: flex; flex-direction: column; }
  .brand-row { display: flex; align-items: center; gap: 5px; }
  .brand-dot { border-radius: 50%; background: var(--red); flex: none; }
  .brand-name { font-weight: 900; color: var(--ink); line-height: 1.05; }
  .brand-slogan { font-weight: 700; color: var(--red); }

  /* Letterhead */
  .letterhead { left: 69px; top: 100px; width: 497px; height: 697px; }
  .letterhead .brand { position: absolute; left: 16px; top: 16px; width: 160px; }
  .letterhead .brand-dot { width: 14px; height: 14px; }
  .letterhead .brand-name { font-size: 15px; }
  .letterhead .brand-slogan { font-size: 8px; margin: 3px 0 0 19px; }
  .services { position: absolute; left: 382px; top: 18px; font-size: 6px; line-height: 1.3; }
  .services-title { color: var(--red); font-weight: 700; }
  .services-sub { font-weight: 700; color: #222; }
  .services ul { list-style: none; font-weight: 700; color: #222; }
  .services li::before { content: "- "; margin-left: 3px; }
  .corner { position: absolute; left: 0; top: 0; width: 100%; height: 100%; }
  .contact { position: absolute; color: #fff; font-weight: 700; line-height: 1.5; white-space: nowrap; }
  .contact .big { font-size: 1.4em; display: flex; align-items: center; gap: 4px; }
  .icon { width: 9px; height: 9px; flex: none; }
  .letterhead .contact { left: 350px; top: 622px; font-size: 6px; }

  /* Card front */
  .card-front { left: 640px; top: 97px; width: 227px; height: 156px; }
  .card-front .band-top { position: absolute; left: 0; top: 0; width: 100%; height: 34px; background: var(--red); }
  .card-front .band-bottom { position: absolute; left: 0; bottom: 0; width: 100%; height: 36px; background: var(--red);
    color: #fff; font-size: 5px; font-weight: 700; text-align: center; padding-top: 6px; line-height: 1.8; }
  .card-front .brand { position: absolute; left: 44px; top: 47px; width: 160px; }
  .card-front .brand-dot { width: 16px; height: 16px; }
  .card-front .brand-name { font-size: 17px; }
  .card-front .brand-slogan { font-size: 8px; margin: 3px 0 0 21px; }

  /* Card back */
  .card-back { left: 640px; top: 300px; width: 227px; height: 160px; }
  .card-back .brand { position: absolute; left: 16px; top: 28px; width: 120px; }
  .card-back .brand-dot { width: 12px; height: 12px; }
  .card-back .brand-name { font-size: 12px; }
  .card-back .brand-slogan { font-size: 6px; margin: 3px 0 0 17px; }
  .card-back .contact { left: 110px; top: 98px; font-size: 5.5px; }
  .card-back .icon { width: 7px; height: 7px; }

  /* Envelope */
  .envelope { left: 640px; top: 583px; width: 497px; height: 214px; }
  .envelope .brand { position: absolute; left: 14px; top: 14px; width: 160px; }
  .envelope .brand-dot { width: 14px; height: 14px; }
  .envelope .brand-name { font-size: 15px; }
  .envelope .brand-slogan { font-size: 7.5px; margin: 3px 0 0 19px; }
  .address-window { position: absolute; left: 53px; top: 125px; width: 249px; height: 62px;
    border-radius: 8px; background: linear-gradient(180deg, #bfbfbf, #e2e2e2); }
</style>
</head>
<body>

<section class="sheet letterhead">
  <svg class="corner" viewBox="0 0 497 697" preserveAspectRatio="none" aria-hidden="true">
    <polygon points="250,697 316,614 392,604 408,588 452,586 468,566 497,548 497,697" fill="var(--edge)"/>
    <polygon points="256,697 320,618 395,608 411,592 455,590 471,570 497,553 497,697" fill="var(--red)"/>
  </svg>
  <div class="brand">
    <div class="brand-row"><span class="brand-dot"></span><span class="brand-name">Harbourgate Locksmiths</span></div>
    <span class="brand-slogan">We come to you 24/7</span>
  </div>
  <div class="services">
    <div class="services-title">MOBILE LOCKSMITH BUSINESS</div>
    <div class="services-sub">Services Offered:</div>
    <ul><li>Residential</li><li>Commercial</li><li>Automotive</li><li>Safes</li></ul>
  </div>
  <div class="contact">
    <div>www.harbourgatelocksmiths.com.au</div>
    <div>dom@harbourgatelocksmiths.com.au</div>
    <div class="big"><svg class="icon" viewBox="0 0 10 10"><rect x="1" y="3" width="8" height="6" rx="1" fill="none" stroke="#fff"/><path d="M1 3 Q5 0 9 3" fill="none" stroke="#fff"/></svg>03 9000 4821</div>
    <div class="big"><svg class="icon" viewBox="0 0 10 10"><rect x="3" y="0.5" width="4.5" height="9" rx="1" fill="none" stroke="#fff"/></svg>0400118342</div>
  </div>
</section>

<section class="sheet card-front">
  <div class="band-top"></div>
  <div class="brand">
    <div class="brand-row"><span class="brand-dot"></span><span class="brand-name">Harbourgate Locksmiths</span></div>
    <span class="brand-slogan">We come to you 24/7</span>
  </div>
  <div class="band-bottom">
    <div>MOBILE LOCKSMITH BUSINESS</div>
    <div>SERVICES OFFERED: RESIDENTIAL, COMMERCIAL, AUTOMOTIVE, SAFES</div>
  </div>
</section>

<section class="sheet card-back">
  <svg class="corner" viewBox="0 0 227 160" preserveAspectRatio="none" aria-hidden="true">
    <polygon points="0,155 68,117 88,91 138,83 153,57 188,45 227,19 227,160 0,160" fill="var(--edge)"/>
    <polygon points="0,160 70,122 90,96 140,88 155,62 190,50 227,25 227,160" fill="var(--red)"/>
  </svg>
  <div class="brand">
    <div class="brand-row"><span class="brand-dot"></span><span class="brand-name">Harbourgate Locksmiths</span></div>
    <span class="brand-slogan">24/7 Fast Reliable Service</span>
  </div>
  <div class="contact">
    <div>www.harbourgatelocksmiths.com.au</div>
    <div>dom@harbourgatelocksmiths.com.au</div>
    <div class="big"><svg class="icon" viewBox="0 0 10 10"><rect x="1" y="3" width="8" height="6" rx="1" fill="none" stroke="#fff"/><path d="M1 3 Q5 0 9 3" fill="none" stroke="#fff"/></svg>03 9000 4821</div>
    <div class="big"><svg class="icon" viewBox="0 0 10 10"><rect x="3" y="0.5" width="4.5" height="9" rx="1" fill="none" stroke="#fff"/></svg>0400118342</div>
  </div>
</section>

<section class="sheet envelope">
  <div class="brand">
    <div class="brand-row"><span class="brand-dot"></span><span class="brand-name">Harbourgate Locksmiths</span></div>
    <span class="brand-slogan">We come to you 24/7</span>
  </div>
  <div class="address-window"></div>
</section>

</body>
</html>
```